Spanish winery needs a label design for a red, white and rosé wine.

We need a front and back label for our representee Vidal Arandes SL, a wine producer in the Spanish region of Extremadura.

Trademark: Sereniza. Sereniza means balanced in English. The message is that the wine show the equilibrium of the blends specially produced for this project, it is balanced in the mounth and nose and it,s a good balance between quality and price.

Target: Wine targets entry level market retail sector in Europe so it cannot be too fancy.

Style: Spanish wines are better seen with a classic touch in the design although a bit of modernity is required.

Number of labels: 3 front and 3 back labels required although you can use the same design and just change the colors. Bottle is a bordeaux style 30 mm high with an screw cup closure, green for the red and transparent for the white and rosé.

Labels size: front max 90 (wide)x130 (high)mm. Back max 85 (w)x85(h)mm.

Information to include in the front label: Trademark, type of wine (red, white or rosé), two short lines of text with tasting notes (see texts on doc file), capacity 75cl, ABV:11º vol. Bottled by Vidal Arandes SL C/Tarifa 27. 06480 Villar del Conde (Badajoz). Spain.

Information to be included in the back label:trademark, type of wine, tasting notes (see texts on doc file), Capacity 75cl, Filling control mark: E, Barcode, Allergy advise, Contains sulfites advise, Pregnant women advise.

Paper: Shiny or matt paper with possibility of foil printing. No embossed effects.

Please see attached Vega Lunar label as a reference of the necessary information to be contained by labels.
Updates

Reason: We would like to give a bit more of time to those that have accepted and have not yet submitted a design.

Target Market(s)

Entry level european consumers

Industry/Entity Type

Retail

Requirements
Nice to have
• Maybe a clasical scale, old coins (balanced in cost).... Balance is the route to follow.

```html
<!DOCTYPE html>
<html lang="en">
<head>
<meta charset="utf-8">
<title>Sereniza Vino Blanco – Front and Back Labels</title>
<link href="https://fonts.googleapis.com/css2?family=Libre+Baskerville&display=swap" rel="stylesheet">
<style>
  :root {
    --page: #ffffff;
    --slate: #5b5b5b;
    --sage: #b8c49a;
    --charcoal: #2b2a28;
    --ink: #2b2a28;
    --paper: #f2f2f2;
    --rule: #8a8a8a;
  }
  * { margin: 0; padding: 0; box-sizing: border-box; }
  html, body {
    width: 1200px; height: 1000px; overflow: hidden;
    background: var(--page);
    font-family: "Libre Baskerville", Georgia, serif;
  }
  .canvas { position: relative; width: 1200px; height: 1000px; }

  /* Front label */
  .front-label {
    position: absolute; left: 145px; top: 202px;
    width: 450px; height: 575px;
  }
  .front-label .brand-band {
    position: absolute; left: 0; top: 0; width: 450px; height: 231px;
    background: var(--slate); color: var(--paper);
  }
  .origin { position: absolute; top: 12px; font-size: 17px; color: var(--paper); }
  .origin--left { left: 8px; }
  .origin--right { right: 8px; top: 10px; }
  .front-label .brand-name {
    position: absolute; left: 0; right: 0; top: 115px;
    text-align: center; font-size: 44px; letter-spacing: 6px; color: var(--paper);
  }
  .front-label .tasting-band {
    position: absolute; left: 0; top: 231px; width: 450px; height: 194px;
    background: var(--sage); color: var(--ink); text-align: center;
  }
  .tasting-band .tasting-note {
    margin: 22px 12px 0; font-size: 20px; line-height: 32px;
  }
  .tasting-band .wine-type {
    margin-top: 18px; font-size: 38px; letter-spacing: 3px;
  }
  .front-label .info-band {
    position: absolute; left: 0; top: 425px; width: 450px; height: 150px;
    background: var(--charcoal); color: var(--paper);
  }
  .info-band .bottler {
    position: absolute; left: 0; right: 0; top: 39px;
    text-align: center; font-size: 12px; line-height: 21px;
  }
  .volume { position: absolute; font-size: 26px; }
  .front-label .volume--left { left: 10px; bottom: 8px; }
  .front-label .volume--left .e-mark { font-size: 32px; }
  .front-label .volume--right { right: 12px; bottom: 9px; }

  /* Back label */
  .back-label {
    position: absolute; left: 623px; top: 233px;
    width: 424px; height: 424px;
    background: var(--charcoal); color: var(--paper);
  }
  .back-label .origin { font-size: 15px; }
  .back-label .origin--left { left: 10px; top: 10px; }
  .back-label .origin--right { right: 10px; top: 8px; }
  .back-label .brand-name {
    position: absolute; left: 0; right: 0; top: 100px;
    text-align: center; font-size: 27px; letter-spacing: 4px;
  }
  .back-label .description {
    position: absolute; left: 0; right: 0; top: 168px;
    text-align: center; font-size: 13.5px; line-height: 20.5px;
  }
  .info-box {
    position: absolute; top: 268px; width: 173px; height: 109px;
    border: 1px solid var(--rule);
    text-align: center; font-size: 14px; padding-top: 13px;
  }
  .info-box--allergy { left: 25px; }
  .info-box--barcode { left: 224px; }
  .back-label .volume { font-size: 16px; bottom: 9px; }
  .back-label .volume--left { left: 11px; }
  .back-label .volume--right { right: 10px; }
</style>
</head>
<body>
<div class="canvas">

  <section class="front-label">
    <header class="brand-band">
      <span class="origin origin--left">PRODUCT</span>
      <span class="origin origin--right">OF SPAIN</span>
      <h1 class="brand-name">SERENIZA</h1>
    </header>
    <div class="tasting-band">
      <p class="tasting-note">A crisp, refreshing Spanish white wine bursting with crisp apple and tropical fruits flavours.</p>
      <h2 class="wine-type">VINO BLANCO</h2>
    </div>
    <footer class="info-band">
      <p class="bottler">Bottled by Vidal Arandes SL C/Tarifa 27.<br>06480 Villar del Conde (Badajoz).<br>Spain.</p>
      <span class="volume volume--left">75cl <span class="e-mark">e</span></span>
      <span class="volume volume--right">11% vol</span>
    </footer>
  </section>

  <section class="back-label">
    <span class="origin origin--left">PRODUCT</span>
    <span class="origin origin--right">OF SPAIN</span>
    <h1 class="brand-name">SERENIZA</h1>
    <p class="description">Sereniza is a deliciously fresh white wine, full of crisp<br>apple and juicy pineapple flavours.<br>It is a great partner to paella or chicken caesar salads.<br>Ready to drink now. Best served chilled.</p>
    <div class="info-box info-box--allergy">Allergy Advice</div>
    <div class="info-box info-box--barcode">Barcode</div>
    <span class="volume volume--left">75cl e</span>
    <span class="volume volume--right">11% vol</span>
  </section>

</div>
</body>
</html>
```